Enlargement project

We would like to create an enlargement of the attached business card design, so that we are able to print hi-res business cards from it,

The end result we are after is an illustrator template that contains hi-res graphics and text that we can edit to insert people's names, job titles, phone and email details

The two colours used within the design are:

Pantone 350 (green)
Panton 484 (red)

The fonts used are;

Futura Medium
Futura Bk BT Italic

Industry/Entity Type

Business

```html
<!DOCTYPE html>
<html lang="en">
<head>
<meta charset="utf-8">
<title>Keenward Business Card</title>
<link rel="stylesheet" href="https://fonts.googleapis.com/css2?family=Jost:ital,wght@0,400;0,500;1,400&display=swap">
<style>
  :root {
    --brand-green: #2c5234;
    --brand-red: #9a3324;
    --artboard-grey: #f4f4f4;
    --card-white: #ffffff;
    --trim-line: #000000;
    --bleed-line: #e8281e;
  }
  * { margin: 0; padding: 0; box-sizing: border-box; }
  html, body {
    width: 1200px;
    height: 755px;
    overflow: hidden;
    background: var(--artboard-grey);
    font-family: "Jost", "Futura", sans-serif;
  }
  .artboard { position: relative; width: 1200px; height: 755px; }
  .bleed-guide {
    position: absolute;
    left: 35px; top: 25px;
    width: 1133px; height: 709px;
    border: 1px solid var(--bleed-line);
  }
  .card {
    position: absolute;
    left: 71px; top: 60px;
    width: 1065px; height: 638px;
    background: var(--card-white);
    border: 1.5px solid var(--trim-line);
    box-shadow: 1px 2px 0 #bdbdbd;
  }
  .brand {
    position: absolute;
    left: 58px; top: 80px;
    display: flex;
    align-items: center;
    gap: 24px;
  }
  .brand-name {
    font-weight: 500;
    font-size: 74px;
    line-height: 1;
    color: var(--brand-green);
    letter-spacing: -0.5px;
  }
  .brand-square {
    width: 150px; height: 150px;
    background: var(--brand-red);
  }
  .contact {
    position: absolute;
    left: 58px;
    color: var(--brand-green);
    font-size: 28px;
    line-height: 35px;
    font-weight: 400;
  }
  .address { top: 271px; }
  .phones { top: 399px; }
  .phones dt { display: inline-block; width: 32px; }
  .phones dd { display: inline; }
  .phones div { white-space: nowrap; }
  .email { top: 520px; }
  .website {
    position: absolute;
    right: 60px; top: 520px;
    color: var(--brand-green);
    font-size: 28px;
    line-height: 35px;
  }
  .person {
    position: absolute;
    left: 720px; top: 262px;
    color: var(--brand-red);
  }
  .person-name {
    font-style: italic;
    font-weight: 400;
    font-size: 45px;
    line-height: 52px;
  }
  .person-title {
    font-size: 29px;
    line-height: 36px;
    margin-left: 3px;
  }
</style>
</head>
<body>
  <div class="artboard">
    <div class="bleed-guide"></div>
    <section class="card">
      <div class="brand">
        <span class="brand-name">Keenward</span>
        <span class="brand-square"></span>
      </div>

      <address class="contact address" style="font-style:normal">
        Suite 4, Level 2<br>
        45 Harbour Lane<br>
        Sydney NSW 2000
      </address>

      <dl class="contact phones">
        <div><dt>t:</dt><dd>02 5550 0140</dd></div>
        <div><dt>f:</dt><dd>02 5550 0141</dd></div>
        <div><dt>d:</dt><dd>02 5550 0142</dd></div>
      </dl>

      <p class="contact email">tharlow@keenward.io</p>

      <div class="person">
        <h1 class="person-name">Tom Harlow</h1>
        <p class="person-title">Technical Operations</p>
      </div>

      <p class="website">www.keenward.io</p>
    </section>
  </div>
</body>
</html>
```